Menu Design Project for new restauranct concept

Design menu for new restaurant concept called Juniper's Burgers & Dogs. Logo is attached.

Industry/Entity Type

Restaurant

Requirements
Must have
• Menu items and pricing:

Burgers
Snack Burger $3.49
Snack Cheeseburger $3.99
Juniper's signature Burger $4.99
Juniper's signature Cheeseburger $5.49
Burger toppings: bacon, lettuce, tomato, onion, pickle, grilled onions, grilled mushrooms, grilled green peppers, jalapeƱo peppers.

Dogs
Hot Dog $2.99
Bacon Cheese Hot Dog $3.99
Slaw Dog $3.99
Kraut Dog $3.49
Chili Dog $3.99 with or with out cheese
Hot dogs are 100% beef

Other
Grilled Chicken Sandwich $5.99
Grilled Chicken Sandwich with cheese $6.49
(Same toppings as burgers)

French Fries $1.99

Loaded Potatos
The Plain Tater: $4.99 choose from: butter, sour cream, cheese, chives
The Garden Tater: $5.99 choose from: the Basic plus, broccoli & cheese, grilled mushrooms, onions, & peppers
The Carver Tater: $6.99 choose from the Basic/Veggie plus: grilled chicken, chili, Philly cheesesteak, pulled pork.

Drinks
32oz. Drink $1.88
20oz. Drink $1.69

attached logo.
Nice to have
• love to incorporate the woodgrain backgound. It makes the logo look most like a cattle brand, which we like.

```html
<!DOCTYPE html>
<html lang="en">
<head>
<meta charset="utf-8">
<title>Juniper's Burgers &amp; Dogs – Menu</title>
<link href="https://fonts.googleapis.com/css2?family=Arvo:ital,wght@0,400;0,700;1,700&family=Rye&display=swap" rel="stylesheet">
<style>
:root{
  --stage:#2a2a2a;
  --label:#f2f2f2;
  --wood-light:#c9bdb8;
  --wood-mid:#a99d98;
  --wood-dark:#8c807b;
  --paper:#efedea;
  --paper-edge:#e2dfdb;
  --ink:#1f1f1f;
  --note:#4a4a4a;
  --heading:#b3262c;
}
*{box-sizing:border-box;margin:0;padding:0}
html,body{width:1200px;height:846px;overflow:hidden;background:var(--stage)}
body{position:relative;font-family:"Arvo",serif;color:var(--ink)}
.side-label{position:absolute;color:var(--label);font-size:18px;font-family:"Arvo",serif;transform:translateX(-50%)}
.side-label.front{left:302px;top:43px}
.side-label.back{left:903px;top:102px}
.card{position:absolute;width:510px;height:660px;box-shadow:6px 8px 14px rgba(0,0,0,.55);overflow:hidden}
.card.front{left:47px;top:85px}
.card.back{left:647px;top:143px}
.wood{position:absolute;inset:0;background:linear-gradient(90deg,var(--wood-mid) 0%,var(--wood-light) 18%,var(--wood-mid) 30%,var(--wood-light) 45%,var(--wood-dark) 55%,var(--wood-light) 68%,var(--wood-mid) 82%,var(--wood-light) 100%)}
.paper{position:absolute;left:23px;top:20px;width:465px;height:623px;background:linear-gradient(180deg,var(--paper),var(--paper-edge))}
.section{position:absolute}
.section h2{font-family:"Rye",serif;font-weight:400;color:var(--heading);font-size:20px;line-height:28px;letter-spacing:-.6px;white-space:nowrap}
.item{display:flex;align-items:baseline;font-weight:700;font-size:11.5px;line-height:20px;white-space:nowrap}
.item .leader{flex:1;border-bottom:1.5px dotted var(--ink);margin:0 2px;transform:translateY(-3px);min-width:6px}
.note{font-style:italic;font-weight:700;font-size:9px;line-height:12px;color:var(--note)}
.burgers{left:42px;top:52px;width:268px}
.dogs{left:42px;top:224px;width:262px}
.other{left:42px;top:384px;width:221px}
.drinks{left:42px;top:518px;width:221px}
.potatoes{left:293px;top:384px;width:175px}
.potatoes .note{margin-bottom:9px}
.other .item.two-line{align-items:flex-start;line-height:18px}
.other .item.two-line .leader{transform:translateY(11px);height:1px}
.other .note{margin:4px 0 2px}
.beef-badge{position:absolute;left:183px;top:208px;width:68px;height:56px}
.brand-mark{position:absolute;left:330px;top:52px;width:137px;height:137px}
.brand-name{position:absolute;left:308px;top:196px;width:180px;text-align:center;font-weight:700;font-size:15px;line-height:18px}
.web-front{position:absolute;left:308px;top:258px;width:180px;text-align:center;font-weight:700;font-size:12px;white-space:nowrap}
.footer{position:absolute;left:42px;top:612px;width:426px;font-weight:700;font-size:9.8px;white-space:nowrap}
.back-mark{position:absolute;left:98px;top:70px;width:316px;height:316px}
.back-name{position:absolute;left:0;top:150px;width:510px;text-align:center;font-weight:700;font-size:44px;line-height:56px;color:var(--ink)}
.web-back{position:absolute;left:0;top:613px;width:510px;text-align:center;font-weight:700;font-size:19px}
</style>
</head>
<body>
<div class="side-label front">Front</div>
<div class="side-label back">Back</div>

<section class="card front">
  <div class="wood" role="img" aria-label="Weathered grey woodgrain plank background"></div>
  <div class="paper"></div>

  <div class="section burgers">
    <h2>Burgers</h2>
    <div class="item"><span>Snack Burger</span><span class="leader"></span><span>$3.49</span></div>
    <div class="item"><span>Snack Cheeseburger</span><span class="leader"></span><span>$3.99</span></div>
    <div class="item"><span>Juniper's signature Burger</span><span class="leader"></span><span>$4.99</span></div>
    <div class="item"><span>Juniper's signature Cheeseburger</span><span class="leader"></span><span>$5.49</span></div>
    <p class="note">Burger toppings: bacon, lettuce, tomato, onion, pickle, grilled onions, grilled mushrooms, grilled green peppers, jalapeño peppers.</p>
  </div>

  <svg class="beef-badge" viewBox="0 0 68 56" role="img" aria-label="Stamp: hot dogs are 100% beef">
    <circle cx="34" cy="28" r="24" fill="none" stroke="#555" stroke-width="2"/>
    <rect x="4" y="24" width="60" height="12" fill="var(--paper)" stroke="#555" stroke-width="1.5"/>
  </svg>

  <div class="section dogs">
    <h2>Dogs</h2>
    <div class="item"><span>Hot Dog</span><span class="leader"></span><span>$2.99</span></div>
    <div class="item"><span>Bacon Cheese Hot Dog</span><span class="leader"></span><span>$3.99</span></div>
    <div class="item"><span>Slaw Dog</span><span class="leader"></span><span>$3.99</span></div>
    <div class="item"><span>Kraut Dog</span><span class="leader"></span><span>$3.49</span></div>
    <div class="item"><span>Chili Dog</span><span class="leader"></span><span>$3.99</span></div>
    <p class="note">with or with out cheese</p>
  </div>

  <div class="section other">
    <h2>Other</h2>
    <div class="item"><span>Grilled Chicken Sandwich</span><span class="leader"></span><span>$5.99</span></div>
    <div class="item two-line"><span>Grilled Chicken Sandwich<br>with cheese</span><span class="leader"></span><span>$6.49</span></div>
    <p class="note">(Same toppings as burgers)</p>
    <div class="item"><span>French Fries</span><span class="leader"></span><span>$1.99</span></div>
  </div>

  <div class="section drinks">
    <h2>Drinks</h2>
    <div class="item"><span>32oz. Drink</span><span class="leader"></span><span>$1.88</span></div>
    <div class="item"><span>20oz. Drink</span><span class="leader"></span><span>$1.69</span></div>
  </div>

  <div class="section potatoes">
    <h2>Loaded Potatoes</h2>
    <div class="item"><span>The Plain Tater</span><span class="leader"></span><span>$4.99</span></div>
    <p class="note">choose from: butter, sour cream, cheese, chives</p>
    <div class="item"><span>The Garden Tater</span><span class="leader"></span><span>$5.99</span></div>
    <p class="note">choose from: the Basic plus, broccoli &amp; cheese, grilled mushrooms, onions &amp; peppers</p>
    <div class="item"><span>The Carver Tater</span><span class="leader"></span><span>$6.99</span></div>
    <p class="note">choose from the Basic/Veggie plus: grilled chicken, chili, Philly cheesesteak, pulled pork</p>
  </div>

  <svg class="brand-mark" viewBox="0 0 137 137" aria-hidden="true">
    <circle cx="68.5" cy="68.5" r="64" fill="none" stroke="var(--ink)" stroke-width="4"/>
  </svg>
  <div class="brand-name">Juniper's<br>Burgers &amp; Dogs</div>
  <div class="web-front">www.junipersburgers.com</div>

  <p class="footer">48 Larch Avenue, Millbrook * Phone: 555 014 2280 * Open hours over here?</p>
</section>

<section class="card back">
  <div class="wood" role="img" aria-label="Weathered grey woodgrain plank background"></div>
  <svg class="back-mark" viewBox="0 0 316 316" aria-hidden="true">
    <circle cx="158" cy="158" r="150" fill="none" stroke="var(--ink)" stroke-width="7"/>
  </svg>
  <div class="back-name">Juniper's<br><br><br><br>Burgers &amp; Dogs</div>
  <div class="web-back">www.junipersburgers.com</div>
</section>
</body>
</html>
```